Harrowden Metal recycling, a business card/logo for our industrial family metal recycling company

A new business card design/logo for our long established family metal recycling company.
I have a logo for our property company which was designed a few months ago on pixel forge which I would like to be very close to this design but have a more industrial feel to it and in a darker blue colour, please see attachments.

Target Market(s)

industries that produce metal waste for recycling, construction sites, engineering companies, manufactures, builders, plumbers, electricians, general house holders.

Industry/Entity Type

Recycling

Contact Information for Business Card

owner/director...Martin harrowden
e-mail....info@harrowdenscrapworks.co.uk
web address.....harrowdenscrapworks.co.uk

Font styles to use
Serif
Sans Serif

Colors
0255a3
ffffff

Requirements
Must have
• -dark blue business card on front.
-white on the back, see contact details, e-mail address for metal company.
-to have an industrial feel to it.
-harrowden logo as business card attached but (harrowden metal recycling)
please remove the little roof/arrow above harrowden as this was relevant to property company.
Nice to have
• please see our website harrowdenscrapworks.co.uk with all details
being correct however I would like to refresh the logo to more like the harrowden property investment business card logo attached.
Should not have
• should not contain details from property investments card as this design is for the metal recycling company.

```html
<!DOCTYPE html>
<html lang="en">
<head>
<meta charset="utf-8">
<title>Harrowden Metal Recycling – Business Card</title>
<link rel="stylesheet" href="https://fonts.googleapis.com/css2?family=Lato:wght@300;400;700;900&display=swap">
<style>
  :root {
    --brand-blue: #2a3887;
    --brand-blue-deep: #232f76;
    --ink: #1b1b1f;
    --text-grey: #2e2e33;
    --paper: #ffffff;
    --backdrop: #5d5d5f;
  }
  * { box-sizing: border-box; margin: 0; padding: 0; }
  html, body { width: 1200px; height: 900px; overflow: hidden; }
  body {
    background: var(--backdrop);
    font-family: "Lato", Arial, sans-serif;
    display: flex;
    flex-direction: column;
    align-items: center;
    justify-content: center;
    gap: 56px;
  }
  .card {
    position: relative;
    width: 640px;
    height: 366px;
    border-radius: 22px;
    overflow: hidden;
    box-shadow: 0 10px 26px rgba(0,0,0,0.35);
  }

  /* Contact side */
  .card--contact { background: var(--paper); }
  .card--contact .swoosh {
    position: absolute; inset: 0; width: 100%; height: 100%;
  }
  .wordmark {
    position: absolute;
    font-weight: 300;
    line-height: 1.05;
    letter-spacing: 1px;
  }
  .wordmark__name { display: block; font-size: 46px; letter-spacing: 2px; }
  .wordmark__tag { display: block; font-size: 14px; letter-spacing: 6px; margin-top: 6px; text-transform: uppercase; }
  .card--contact .wordmark { left: 44px; top: 74px; color: var(--ink); }

  .divider {
    position: absolute;
    width: 1.5px;
  }
  .card--contact .divider { left: 318px; top: 70px; height: 150px; background: var(--brand-blue); }

  .contact {
    position: absolute;
    left: 344px;
    top: 66px;
    color: var(--text-grey);
  }
  .contact__name { font-size: 27px; font-weight: 900; color: var(--ink); letter-spacing: -0.3px; }
  .contact__name .first { color: var(--brand-blue); }
  .contact__role { font-size: 15px; margin-top: 2px; }
  .contact__address { font-size: 15px; margin-top: 10px; line-height: 1.3; }
  .contact__list { list-style: none; margin-top: 4px; }
  .contact__list li { display: flex; align-items: center; gap: 8px; font-size: 15px; line-height: 1.45; }
  .contact__list svg { width: 13px; height: 13px; flex: none; fill: var(--brand-blue); }

  /* Services side */
  .card--services { background: var(--brand-blue); color: var(--paper); }
  .card--services .wordmark { left: 44px; top: 112px; color: var(--paper); }
  .card--services .divider { left: 348px; top: 104px; height: 160px; background: var(--paper); }
  .services {
    position: absolute;
    left: 378px;
    top: 116px;
    list-style: none;
  }
  .services li {
    font-size: 19px;
    font-weight: 400;
    line-height: 1.5;
    text-transform: uppercase;
    letter-spacing: 0.2px;
    display: flex;
    align-items: center;
    gap: 10px;
  }
  .services li::before {
    content: "";
    width: 6px; height: 6px;
    border-radius: 50%;
    background: var(--paper);
  }
</style>
</head>
<body>

  <section class="card card--contact" aria-label="Contact side">
    <svg class="swoosh" viewBox="0 0 640 366" preserveAspectRatio="none" aria-hidden="true">
      <path d="M0 110 C 40 150, 50 250, 120 300 C 200 350, 330 360, 420 366 L0 366 Z" fill="var(--brand-blue)"/>
      <path d="M0 360 C 100 300, 200 300, 330 330 C 380 342, 420 352, 470 366 L0 366 Z" fill="var(--brand-blue)"/>
      <path d="M60 200 C 110 290, 220 320, 470 366" fill="none" stroke="var(--ink)" stroke-width="5"/>
      <path d="M50 194 C 100 296, 210 334, 440 366" fill="none" stroke="var(--brand-blue)" stroke-width="3"/>
    </svg>

    <div class="wordmark">
      <span class="wordmark__name">Harrowden</span>
      <span class="wordmark__tag">Metal Recycling</span>
    </div>

    <div class="divider"></div>

    <div class="contact">
      <p class="contact__name"><span class="first">Martin</span> Harrowden</p>
      <p class="contact__role">Owner/Director</p>
      <p class="contact__address">Unit 7, 14B Kestrel Lane,<br>Northfield, NF4 2QT</p>
      <ul class="contact__list">
        <li>
          <svg viewBox="0 0 24 24" aria-hidden="true"><path d="M6.6 10.8a15.1 15.1 0 0 0 6.6 6.6l2.2-2.2c.3-.3.7-.4 1-.2 1.1.4 2.3.6 3.6.6.6 0 1 .4 1 1V20c0 .6-.4 1-1 1C10.6 21 3 13.4 3 4c0-.6.4-1 1-1h3.5c.6 0 1 .4 1 1 0 1.3.2 2.5.6 3.6.1.3 0 .7-.2 1z"/></svg>
          020-5550-0148
        </li>
        <li>
          <svg viewBox="0 0 24 24" aria-hidden="true"><path d="M2 5h20v14H2z M4 7v.4l8 5.2 8-5.2V7z" fill-rule="evenodd"/></svg>
          info@harrowdenscrapworks.co.uk
        </li>
        <li>
          <svg viewBox="0 0 24 24" aria-hidden="true"><circle cx="12" cy="12" r="10"/><path d="M2 12h20M12 2c3 3 3 17 0 20M12 2c-3 3-3 17 0 20" fill="none" stroke="#fff" stroke-width="1.5"/></svg>
          www.harrowdenscrapworks.co.uk
        </li>
      </ul>
    </div>
  </section>

  <section class="card card--services" aria-label="Services side">
    <div class="wordmark">
      <span class="wordmark__name">Harrowden</span>
      <span class="wordmark__tag">Metal Recycling</span>
    </div>

    <div class="divider"></div>

    <ul class="services">
      <li>Instant Cash</li>
      <li>Fast Bank Transfer</li>
      <li>Pre Paid Vantra Card</li>
      <li>Printed Cheque</li>
    </ul>
  </section>

</body>
</html>
```